Wedding and event Photography company.

We need a business card design for a photography company based in Singapore named TamKeza. Our core service offering is wedding photojournalism. We would like to see minimalistic designs that use the colour white. The final design should communicate a sense of ease and reliability.

The attached are a couple of visual reference which i found over the web, i hope it will helps.

Project Brief Update (14th July 2014):
- Please refrain from using any images from the website for the design. The laws and regulations over here does not allow me to distribute my client's images. Thanks!

Target Market(s)

Young and middle aged adults aged 24 - 38. With money to spend =D

Industry/Entity Type

Business

Contact Information for Business Card

Name: Dev Lunor
Designation: Head Photographer
Mobile: +65 81749026
Email: jun@tamkeza.example
Website: www.tamkeza.example

Font styles to use
Other font styles liked:
• Baskerville URW

Colors

Designer to choose colors to be used in the design.

Requirements
Must have
• Must include:
• - The brand TamKeza
• - The logo attached
• - Please help to place the brand TamKeza with the logo according to your preferences.
• - Services
• - Wedding Photography
• - Portraiture
• - Photojournalism
Nice to have
• Looking forward to an elegant and simple design. Please see attached examples!
• Please use Serif Fonts
Should not have
• Please refrain from using dark tones for the majority of the design.
• Please refrain from letterpress and embossing.

```html
<!DOCTYPE html>
<html lang="en">
<head>
<meta charset="utf-8">
<title>TamKeza Photography — Business Card</title>
<link rel="stylesheet" href="https://fonts.googleapis.com/css2?family=Libre+Baskerville:wght@400;700&display=swap">
<style>
  :root {
    --backdrop: #dcdcdc;
    --card: #ffffff;
    --ink: #111111;
    --ink-soft: #8a8a8a;
    --mark-tone-a: #e4e4e4;
    --mark-tone-b: #f7f7f7;
    --card-shadow: rgba(0, 0, 0, 0.18);
  }
  * { box-sizing: border-box; margin: 0; padding: 0; }
  html, body {
    width: 1200px;
    height: 800px;
    overflow: hidden;
    background: var(--backdrop);
    font-family: "Libre Baskerville", "Baskerville", serif;
    color: var(--ink);
  }
  .canvas {
    width: 1200px;
    height: 800px;
    display: flex;
    align-items: center;
    justify-content: center;
    gap: 40px;
  }
  .card {
    position: relative;
    width: 540px;
    height: 309px;
    background: var(--card);
    box-shadow: 0 3px 10px var(--card-shadow);
    overflow: hidden;
  }

  /* Front */
  .brand {
    position: absolute;
    left: 0;
    right: 0;
    top: 92px;
    text-align: center;
  }
  .brand-name {
    display: inline-flex;
    align-items: center;
    gap: 10px;
    font-size: 30px;
    letter-spacing: 0.01em;
  }
  .brand-dot {
    width: 14px;
    height: 14px;
    border-radius: 50%;
    background: var(--ink);
  }
  .brand-tagline {
    margin-top: 8px;
    font-size: 12px;
    letter-spacing: 0.22em;
    color: var(--ink-soft);
  }
  .services {
    position: absolute;
    left: 30px;
    right: 30px;
    bottom: 30px;
    display: flex;
    justify-content: space-between;
    list-style: none;
    font-size: 12px;
    letter-spacing: 0.06em;
    color: var(--ink-soft);
  }
  .service {
    display: flex;
    align-items: center;
    gap: 8px;
  }
  .service::before {
    content: "";
    width: 8px;
    height: 8px;
    border-radius: 50%;
    background: var(--ink);
  }

  /* Back */
  .brand-mark-area {
    position: absolute;
    right: -30px;
    top: -70px;
    width: 260px;
    height: 260px;
    border-radius: 50%;
    background: radial-gradient(circle at 45% 55%, var(--mark-tone-a), var(--mark-tone-b) 72%);
  }
  .person {
    position: absolute;
    left: 32px;
    top: 118px;
  }
  .person-name {
    font-size: 28px;
    line-height: 1;
  }
  .person-role {
    margin-top: 6px;
    font-size: 12px;
    letter-spacing: 0.18em;
    color: var(--ink-soft);
  }
  .contacts {
    position: absolute;
    left: 60px;
    top: 196px;
    list-style: none;
    font-size: 12px;
    letter-spacing: 0.04em;
  }
  .contact {
    display: flex;
    align-items: center;
    gap: 12px;
    height: 22px;
  }
  .contact svg {
    width: 13px;
    height: 13px;
    fill: var(--ink);
    flex: none;
  }
  .registration {
    position: absolute;
    right: 30px;
    bottom: 26px;
    font-size: 11px;
    letter-spacing: 0.08em;
    color: var(--ink-soft);
  }
</style>
</head>
<body>
  <main class="canvas">
    <section class="card card-front" aria-label="Business card front">
      <div class="brand">
        <div class="brand-name"><span class="brand-dot"></span>TamKeza</div>
        <div class="brand-tagline">PHOTOGRAPHY</div>
      </div>
      <ul class="services">
        <li class="service">Wedding Photography</li>
        <li class="service">Portraiture</li>
        <li class="service">Photojournalism</li>
      </ul>
    </section>

    <section class="card card-back" aria-label="Business card back">
      <div class="brand-mark-area" role="img" aria-label="Large brush-stroke brand mark decoration"></div>
      <div class="person">
        <div class="person-name">Dev Lunor</div>
        <div class="person-role">PHOTOGRAPHER</div>
      </div>
      <ul class="contacts">
        <li class="contact">
          <svg viewBox="0 0 24 24" aria-hidden="true"><path d="M6.6 10.8a15.1 15.1 0 0 0 6.6 6.6l2.2-2.2a1 1 0 0 1 1-.25 11.4 11.4 0 0 0 3.6.57 1 1 0 0 1 1 1V20a1 1 0 0 1-1 1A17 17 0 0 1 3 4a1 1 0 0 1 1-1h3.5a1 1 0 0 1 1 1c0 1.25.2 2.46.57 3.58a1 1 0 0 1-.25 1z"/></svg>
          <span>+65 81749026</span>
        </li>
        <li class="contact">
          <svg viewBox="0 0 24 24" aria-hidden="true"><path d="M2 5h20v14H2zm2 2v.4l8 5.2 8-5.2V7zm0 2.8V17h16V9.8l-8 5.2z"/></svg>
          <span>jun@tamkeza.example</span>
        </li>
        <li class="contact">
          <svg viewBox="0 0 24 24" aria-hidden="true"><path d="M12 2a10 10 0 1 0 0 20 10 10 0 0 0 0-20zm6.9 6h-3a15.6 15.6 0 0 0-1.4-3.6A8 8 0 0 1 18.9 8zM12 4c.8 1.2 1.5 2.5 1.9 4h-3.8c.4-1.5 1.1-2.8 1.9-4zM4.3 14a8.2 8.2 0 0 1 0-4h3.4a16 16 0 0 0 0 4zm.8 2h3a15.6 15.6 0 0 0 1.4 3.6A8 8 0 0 1 5.1 16zm3-8h-3a8 8 0 0 1 4.4-3.6A15.6 15.6 0 0 0 8.1 8zM12 20c-.8-1.2-1.5-2.5-1.9-4h3.8c-.4 1.5-1.1 2.8-1.9 4zm2.3-6H9.7a14.7 14.7 0 0 1 0-4h4.6a14.7 14.7 0 0 1 0 4zm.2 5.6a15.6 15.6 0 0 0 1.4-3.6h3a8 8 0 0 1-4.4 3.6zm1.8-5.6a16 16 0 0 0 0-4h3.4a8.2 8.2 0 0 1 0 4z"/></svg>
          <span>www.tamkeza.example</span>
        </li>
      </ul>
      <div class="registration">Business Reg No: 52817604K</div>
    </section>
  </main>
</body>
</html>
```